依頼詳細
当店の名物は地酒と鮮度の良いお刺身と生本まぐろの分厚いお刺身、ホタテやサザエ、ハマグリなどの浜焼きです。ご家族連れやおひとりさままで幅広い方に当店のウリである鮮度感が伝わるような看板を希望しております。よろしくお願いいたします。
記載項目
さかなや ゆめたか
希望イメージ
シンプル 複雑
単色 カラフル
暗い 明るい
日常 高級
遊び心 厳粛
未来的 伝統的
女性的 男性的
希望する色
青系、茶系、無彩色系
納品ファイル
• 高解像度JPG (.jpg)
補足説明
看板のサイズが分からず問い合わせ中です。
添付の画像くらいのイメージです。
■ 選んだ理由

とにかくデザインが素敵でした!
既存のイメージと違い綺麗すぎて少し悩みましたが、新しいことに挑戦するので思いきってロゴのイメージも変えてみよう!また素敵なイメージに負けないようなお店にしなければ!と背中を押していただいた気がします。

■ 提案者全員のお礼・コメント

既存のイメージを大切にしていただいた素敵なデザインをご応募いただき嬉しく思いました。
ありがとうございました。

```html
<!DOCTYPE html>
<html lang="ja">
<head>
<meta charset="utf-8">
<title>さかなや ゆめたか 看板デザイン</title>
<link rel="stylesheet" href="https://fonts.googleapis.com/css2?family=Yuji+Boku&family=Yuji+Syuku&family=Noto+Sans+JP:wght@500&display=swap">
<style>
  :root {
    --paper: #ffffff;
    --ink: #141414;
    --sea-blue: #1d5ea8;
    --tag-red: #d9232b;
    --shell-tone: #a08773;
    --tuna-tone: #4b5a6b;
    --frame: #c9c9c9;
  }
  * { margin: 0; padding: 0; box-sizing: border-box; }
  html, body { width: 846px; height: 1200px; overflow: hidden; background: var(--paper); }
  .canvas { position: relative; width: 846px; height: 1200px; background: var(--paper); }

  .sign { position: absolute; background: var(--paper); border: 2px solid var(--frame); overflow: hidden; }
  .sign--wide { left: 62px; top: 108px; width: 722px; height: 248px; }
  .sign--tall { left: 268px; top: 424px; width: 310px; height: 708px; }

  .waves { position: absolute; display: block; }
  .art { position: absolute; border-radius: 46%; }
  .art--shells { background: linear-gradient(135deg, #c7b3a2, var(--shell-tone)); }
  .art--tuna { background: linear-gradient(160deg, #7b8a9b, var(--tuna-tone) 60%, #c9d2db); border-radius: 50% 40% 45% 55%; }

  .tag {
    position: absolute; background: var(--tag-red); color: var(--paper);
    font-family: "Yuji Syuku", serif; display: flex; align-items: center; justify-content: center;
    border-radius: 6px; transform: rotate(-8deg); white-space: nowrap; line-height: 1;
  }
  .shop-kana { position: absolute; font-family: "Yuji Boku", serif; color: var(--ink); line-height: 1; white-space: nowrap; }
  .shop-name { position: absolute; font-family: "Yuji Boku", serif; font-weight: 400; color: var(--ink); line-height: 1; white-space: nowrap; }
  .shop-roman { position: absolute; font-family: "Noto Sans JP", sans-serif; font-weight: 500; color: var(--ink); letter-spacing: 3px; line-height: 1; }
  .vertical { writing-mode: vertical-rl; }

  /* wide sign */
  .sign--wide .waves { left: 0; top: 0; width: 722px; height: 248px; }
  .sign--wide .tag { left: 36px; top: 34px; width: 128px; height: 44px; font-size: 26px; }
  .sign--wide .art--shells { left: 28px; top: 100px; width: 140px; height: 70px; }
  .sign--wide .art--tuna { left: 580px; top: 24px; width: 130px; height: 150px; }
  .sign--wide .shop-kana { left: 282px; top: 16px; font-size: 48px; letter-spacing: 6px; }
  .sign--wide .shop-name { left: 190px; top: 82px; font-size: 92px; }
  .sign--wide .shop-roman { left: 318px; top: 196px; font-size: 18px; }

  /* tall sign */
  .sign--tall .waves { left: 0; top: 0; width: 310px; height: 708px; }
  .sign--tall .tag { left: 14px; top: 34px; width: 112px; height: 42px; font-size: 23px; }
  .sign--tall .art--shells { left: 140px; top: 30px; width: 62px; height: 96px; }
  .sign--tall .shop-kana { left: 196px; top: 140px; font-size: 50px; letter-spacing: 6px; }
  .sign--tall .shop-name { left: 30px; top: 128px; font-size: 114px; letter-spacing: -2px; }
  .sign--tall .art--tuna { left: 166px; top: 430px; width: 130px; height: 210px; }
</style>
</head>
<body>
<main class="canvas">

  <section class="sign sign--wide" aria-label="横型看板">
    <svg class="waves" viewBox="0 0 722 248" role="img" aria-label="青海波の波模様">
      <path d="M0 190 Q120 166 240 188 T480 186 Q560 170 620 150 Q680 136 722 150 L722 248 L0 248 Z" fill="var(--sea-blue)"/>
    </svg>
    <div class="art art--shells" role="img" aria-label="サザエとハマグリのイラスト"></div>
    <div class="art art--tuna" role="img" aria-label="まぐろのイラスト"></div>
    <div class="tag">お食事処</div>
    <p class="shop-kana">さかなや</p>
    <h1 class="shop-name">ゆめたか</h1>
    <p class="shop-roman">YUMETAKA</p>
  </section>

  <section class="sign sign--tall" aria-label="縦型看板">
    <svg class="waves" viewBox="0 0 310 708" role="img" aria-label="青海波の波模様">
      <path d="M130 40 Q220 20 310 50 L310 130 Q220 150 130 120 Z" fill="var(--sea-blue)"/>
      <path d="M0 600 Q80 570 160 600 Q240 620 310 590 L310 708 L0 708 Z" fill="var(--sea-blue)"/>
    </svg>
    <div class="art art--shells" role="img" aria-label="サザエとハマグリのイラスト"></div>
    <div class="tag">お食事処</div>
    <p class="shop-kana vertical">さかなや</p>
    <h2 class="shop-name vertical">ゆめたか</h2>
    <div class="art art--tuna" role="img" aria-label="まぐろのイラスト"></div>
  </section>

</main>
</body>
</html>
```